I would like a minimalist clean and uncluttered website design.
Initially, I would like to see a front page only and would then like to build on the project front there.
RTV logo file with no background is attached, can be grey scale if the designer wishes.
I would like the front page to speak about the company's ethos and goals and I will need to put a great deal of thought into this to ensure it has the desired impact with the content on the subsequent pages.
The paragraph below gives a bit of an idea as to what this will include.
"RTV is a technology company providing approachable IT products and services to business:
With the overwhelming advancements in technology, businesses often find it difficult to determine what is available and what best suits their businesses specific needs.
We can assist business with their IT infrustucture, devices, software in procurement, installation, training, cost control as well as ongoing administration and support. We also keep our Clients informed of new technology and products which can benefit them"
Target Market(s)
Business, Health, Education, Professional Practices. Target age would be around 30 plus either male or female. Office administration level through Managing Directors. English speaking.

```html
<!DOCTYPE html>
<html lang="en">
<head>
<meta charset="utf-8">
<title>RTV – Home</title>
<link href="https://fonts.googleapis.com/css2?family=Questrial&family=Open+Sans:ital,wght@0,300;0,400;1,300&display=swap" rel="stylesheet">
<style>
:root{
  --navy:#344a85;
  --navy-dark:#253a6e;
  --green:#8dbb45;
  --text:#6b6b6b;
  --nav:#4a4a4a;
  --muted:#9a9a9a;
  --line:#dcdcdc;
  --hero:#ececec;
  --footer:#f2f2f2;
  --white:#ffffff;
}
*{margin:0;padding:0;box-sizing:border-box}
html,body{width:1200px;height:930px;overflow:hidden;background:var(--white)}
body{position:relative;font-family:"Open Sans",sans-serif;color:var(--text)}
.header{position:absolute;left:0;top:0;width:1200px;height:67px;border-bottom:1px solid var(--line);background:var(--white)}
.brand{position:absolute;left:201px;top:14px;display:flex;align-items:center;gap:8px}
.brand-mark{width:30px;height:30px;background:var(--green)}
.brand-name{font-family:"Questrial",sans-serif;font-size:30px;color:var(--navy);letter-spacing:3px}
.nav{position:absolute;top:0;left:484px;height:67px;font-family:"Questrial",sans-serif;font-size:13.5px;color:var(--nav)}
.nav a{color:inherit;text-decoration:none;position:absolute;top:25px;white-space:nowrap}
.nav a.active{color:var(--green)}
.nav .underline{position:absolute;left:0;top:64px;width:78px;height:3px;background:var(--green)}
.account{position:absolute;top:28px;left:900px;font-family:"Questrial",sans-serif;font-size:10px;color:var(--muted);display:flex;gap:10px;align-items:center}
.account .sep{width:1px;height:12px;background:var(--line)}
.hero{position:absolute;left:0;top:67px;width:1200px;height:373px;background:var(--hero);border-bottom:1px solid #d6d6d6;overflow:hidden}
.hero-photo{position:absolute;left:380px;top:0;width:700px;height:373px;background:linear-gradient(90deg,rgba(236,236,236,1) 0%,#d9d6d2 30%,#cfcbe0 65%,#e6e3ee 90%,rgba(236,236,236,1) 100%)}
.hero-title{position:absolute;left:197px;top:110px;font-family:"Questrial",sans-serif;font-size:27px;line-height:34px;color:var(--navy);font-weight:400;white-space:nowrap}
.hero-lead{position:absolute;left:197px;top:149px;width:340px;font-size:15.5px;font-style:italic;font-weight:300;line-height:22px;color:#777}
.btn{position:absolute;left:197px;top:215px;width:109px;height:30px;background:var(--green);color:var(--white);font-family:"Questrial",sans-serif;font-size:12px;line-height:30px;text-align:center}
.dots{position:absolute;left:197px;top:303px;display:flex;gap:2px}
.dot{width:14px;height:14px;border:1px solid #b5b5b5;border-radius:50%;background:var(--white);position:relative}
.dot.current::after{content:"";position:absolute;left:3px;top:3px;width:6px;height:6px;border-radius:50%;background:var(--navy)}
.ribbon{position:absolute;left:446px;top:480px}
.ribbon-title{position:absolute;left:29px;top:0;width:215px;height:37px;background:var(--navy);color:var(--white);font-family:"Questrial",sans-serif;font-size:24px;text-align:center;line-height:37px;box-shadow:0 3px 0 #fff,0 4px 0 rgba(0,0,0,.06)}
.services{position:absolute;left:197px;top:582px;width:840px;display:grid;grid-template-columns:292px 292px 256px;row-gap:40px}
.service-head{display:flex;align-items:center;gap:9px;height:24px}
.service-head h3{font-family:"Questrial",sans-serif;font-weight:400;font-size:17px;color:var(--navy)}
.service-head svg{fill:var(--navy)}
.service p{margin-top:13px;font-size:10.5px;line-height:13.7px;width:215px}
.footer{position:absolute;left:0;top:840px;width:1200px;height:90px;background:var(--footer);border-top:1px solid #e6e6e6}
.footer-links{position:absolute;left:195px;top:33px;font-size:10px;color:var(--text)}
.footer-links span{margin:0 5px;color:#aaa}
.social{position:absolute;left:927px;top:35px;display:flex;gap:4px}
.social i{width:16px;height:16px;border-radius:50%;background:#666;display:block}
</style>
</head>
<body>
<header class="header">
  <div class="brand"><span class="brand-mark"></span><span class="brand-name">RTV</span></div>
  <nav class="nav">
    <a class="active" style="left:20px">Home</a>
    <a style="left:91px">Services</a>
    <a style="left:176px">Project</a>
    <a style="left:253px">Articles</a>
    <a style="left:332px">Contact</a>
    <span class="underline"></span>
  </nav>
  <div class="account"><span>Log in</span><span class="sep"></span><span>Sign up</span></div>
</header>

<section class="hero">
  <div class="hero-photo" role="img" aria-label="Smiling businesswoman in a lilac shirt with colleagues blurred in an office behind her"></div>
  <h1 class="hero-title">Welcome to RapidTechVault</h1>
  <p class="hero-lead">RTV is a technology company providing approachable IT products and services to business.</p>
  <a class="btn">LEARN MORE</a>
  <div class="dots"><span class="dot"></span><span class="dot current"></span><span class="dot"></span><span class="dot"></span></div>
</section>

<div class="ribbon">
  <svg width="273" height="46" viewBox="0 0 273 46">
    <polygon points="0,8 36,8 36,46 8,46 16,27" fill="var(--navy-dark)"/>
    <polygon points="273,8 237,8 237,46 265,46 257,27" fill="var(--navy-dark)"/>
  </svg>
  <div class="ribbon-title">OUR SERVICES</div>
</div>

<section class="services">
  <div class="service">
    <div class="service-head"><svg width="22" height="20" viewBox="0 0 22 20"><path d="M1 1h20v14H1z M3 3v10h16V3z M9 15h4v2h3v2H6v-2h3z"/></svg><h3>IT infrustucture</h3></div>
    <p>Lorem Ipsum is simply dummy text of the printing and typesetting industry. Lorem Ipsum dummy text ever since the 1500s...</p>
  </div>
  <div class="service">
    <div class="service-head"><svg width="16" height="20" viewBox="0 0 16 20"><path d="M1 0h14v20H1z M3 2v14h10V2z"/></svg><h3>Devices</h3></div>
    <p>Lorem Ipsum is simply dummy text of the printing and typesetting industry. Lorem Ipsum dummy text ever since the 1500s...</p>
  </div>
  <div class="service">
    <div class="service-head"><svg width="22" height="20" viewBox="0 0 22 20"><path d="M11 0l11 5-11 5L0 5z M0 7l10 5v8L0 15z M22 7l-10 5v8l10-5z"/></svg><h3>Software</h3></div>
    <p>Lorem Ipsum is simply dummy text of the printing and typesetting industry. Lorem Ipsum dummy text ever since the 1500s...</p>
  </div>
  <div class="service">
    <div class="service-head"><svg width="18" height="22" viewBox="0 0 18 22"><path d="M1 0h16v2h-2c0 5-5 7-5 9s5 4 5 9h2v2H1v-2h2c0-5 5-7 5-9S3 7 3 2H1z M5 2c0 4 4 6 4 8 0-2 4-4 4-8z"/></svg><h3>Installation</h3></div>
    <p>Lorem Ipsum is simply dummy text of the printing and typesetting industry. Lorem Ipsum dummy text ever since the 1500s...</p>
  </div>
  <div class="service">
    <div class="service-head"><svg width="20" height="22" viewBox="0 0 20 22"><path d="M4 12V3h2v7h1V1h2v9h1V2h2v8h1V5h2v9c0 4-3 7-7 7-3 0-5-2-7-6l-2-4 2-1z"/></svg><h3>Training</h3></div>
    <p>Lorem Ipsum is simply dummy text of the printing and typesetting industry. Lorem Ipsum dummy text ever since the 1500s...</p>
  </div>
  <div class="service">
    <div class="service-head"><svg width="30" height="20" viewBox="0 0 30 20"><path d="M4 0h26v14h-2V2H4z M0 4h27v16H0z M2 6v12h23V6z M13.5 8a4 4 0 1 1 0 8a4 4 0 1 1 0-8z"/></svg><h3>Cost control</h3></div>
    <p>Lorem Ipsum is simply dummy text of the printing and typesetting industry. Lorem Ipsum dummy text ever since the 1500s...</p>
  </div>
</section>

<footer class="footer">
  <div class="footer-links">Home<span>|</span>Services<span>|</span>Project<span>|</span>Articles<span>|</span>Contact<span>|</span>Copyright © 2013 RapidTechVault.</div>
  <div class="social"><i></i><i></i><i></i><i></i></div>
</footer>
</body>
</html>
```